Hello my name is Colin, I am Starting a business called Harbor Health and fitness and am in need of a memorable business card.
It is a personal training studio. I have added the logo that i would like to be on the left center om my business card. i would like room left up the top for a heading sentence such as. "Is your body shocking for all the wrong reasons". there must be room left on the right of the logo below the main heading for 3 sub headings.
then under those 3 headings and logo room for another larger heading eg. "give me a call and learn how to eat chocolate, drink bear and have great sex". in what room is left i would like to be used for my contact details, use I'm Colin Pettersby your fitness expert on the left then on the right Phone, Email and website space in at least 12 Point. Very specific i know :) now onto the back, for the back i would like an eye catching graphic and room for one main headline and 3 bullet points centered just write anything i will choose what to put in them when i pick a winner. Thank you very much for sticking through all of that :) i appreciate you taking the time to read it and hopefully undergo designing me a business card.
I can't wait to see the designs!

Target Market(s)

slightly more towards females although it would probably be best if it was targeted towards both sexes

Industry/Entity Type

Training

Requirements
Nice to have
• I would love to see if anyone could come up with a design that would really make my card stand out and be memorable.
Should not have
• tacky fitness photos of abs and muscles etc.

```html
<!DOCTYPE html>
<html lang="en">
<head>
<meta charset="utf-8">
<title>Harbor Health and Fitness – Business Cards</title>
<link href="https://fonts.googleapis.com/css2?family=Arimo:ital,wght@0,400;0,700;1,400;1,700&family=Source+Sans+3:wght@400;600&display=swap" rel="stylesheet">
<style>
  :root {
    --ink-blue: #1b37a6;
    --ink-grey: #333333;
    --faint: #eceef2;
    --card-border: #111111;
    --white: #ffffff;
    --choc-dark: #1a1413;
    --choc-mid: #5a3322;
    --skin: #d9a48a;
    --sea-dark: #0f2a4a;
    --sea-mid: #2f6aa6;
  }
  html, body {
    margin: 0;
    padding: 0;
    width: 1200px;
    height: 1000px;
    overflow: hidden;
    background: var(--white);
  }
  .canvas { position: relative; width: 1200px; height: 1000px; }

  /* Front card */
  .card-front {
    position: absolute;
    left: 414px; top: 253px;
    width: 390px; height: 216px;
    border: 1px solid var(--card-border);
    background: var(--white);
    overflow: hidden;
    font-family: "Arimo", Arial, sans-serif;
    color: var(--ink-blue);
  }
  .bg-brand {
    position: absolute; left: 44px; top: 88px;
    font-family: "Arimo", Arial, sans-serif;
    color: var(--faint);
    line-height: 1;
  }
  .bg-brand .bg-name { font-size: 78px; font-weight: 400; letter-spacing: 2px; }
  .bg-brand .bg-tag { position: absolute; left: 78px; top: 80px; font-size: 22px; white-space: nowrap; }
  .front-heading {
    position: absolute; left: 0; right: 0; top: 26px;
    text-align: center;
    font-family: "Source Sans 3", "Myriad Pro", sans-serif;
    font-weight: 600; font-size: 15px;
    color: var(--ink-grey);
  }
  .brand {
    position: absolute; left: 41px; top: 60px;
    width: 104px; text-align: center;
  }
  .brand-name { font-size: 30px; font-weight: 400; line-height: 1; color: var(--ink-blue); }
  .brand-tag { font-size: 8px; color: var(--ink-grey); margin-top: 2px; }
  .mottos {
    position: absolute; left: 51px; top: 124px;
    margin: 0; padding: 0; list-style: none;
    font-style: italic; font-size: 14px; line-height: 16px;
  }
  .identity {
    position: absolute; left: 176px; top: 61px; width: 180px;
    text-align: center;
  }
  .identity-name { font-size: 17px; line-height: 20px; }
  .identity-role { font-size: 18px; font-weight: 700; font-style: italic; line-height: 20px; white-space: nowrap; }
  .contact {
    position: absolute; left: 176px; top: 116px; width: 176px;
    text-align: center; font-size: 15px; line-height: 18px;
  }
  .contact .phone { font-size: 18px; line-height: 22px; }

  /* Back cards */
  .card-back {
    position: absolute; top: 497px;
    width: 392px; height: 217px;
    overflow: hidden;
    color: var(--white);
  }
  .card-back .photo { position: absolute; inset: 0; }
  .card-back-choc { left: 212px; }
  .card-back-choc .photo {
    background: linear-gradient(90deg, var(--choc-dark) 0%, var(--choc-dark) 34%, var(--choc-mid) 55%, var(--skin) 78%, #b9683d 100%);
  }
  .choc-copy {
    position: absolute; left: 26px; top: 38px;
    font-family: "Arimo", Arial, sans-serif;
  }
  .choc-copy .lead { font-size: 17px; font-weight: 700; text-align: center; width: 92px; line-height: 24px; }
  .choc-copy .sub { font-size: 15px; font-weight: 700; margin-top: 2px; line-height: 20px; }
  .choc-copy ul { margin: 2px 0 0; padding: 0; list-style: none; font-size: 15px; line-height: 19px; }

  .card-back-sea { left: 622px; width: 390px; }
  .card-back-sea .photo {
    background: linear-gradient(90deg, #c99a7a 0%, #d8b49a 26%, var(--sea-mid) 48%, var(--sea-dark) 100%);
  }
  .sea-copy {
    position: absolute; left: 196px; top: 31px; width 160px;
    width: 162px; text-align: center;
    font-family: "Source Sans 3", "Myriad Pro", sans-serif;
    font-weight: 600; font-size: 17px; line-height: 22.5px;
  }
  .sea-brand {
    position: absolute; left: 300px; top: 165px;
    font-family: "Arimo", Arial, sans-serif;
    font-size: 19px; color: var(--ink-blue); line-height: 1;
  }
</style>
</head>
<body>
<div class="canvas">

  <section class="card-front">
    <div class="bg-brand" aria-hidden="true">
      <div class="bg-name">Harbor</div>
      <div class="bg-tag">Health and Fitness</div>
    </div>
    <p class="front-heading" style="margin:0">Is your body shocking for all the wrong reasons?</p>
    <div class="brand">
      <div class="brand-name">Harbor</div>
      <div class="brand-tag">Health and Fitness</div>
    </div>
    <ul class="mottos">
      <li>* Never give up</li>
      <li>* Work for it</li>
      <li>* Let them jealous</li>
    </ul>
    <div class="identity">
      <div class="identity-name">Colin Pettersby</div>
      <div class="identity-role">Your Fitness Expert</div>
    </div>
    <div class="contact">
      <div class="phone">555 0142 800</div>
      <div>colin@pettersby.com</div>
      <div>www.pettersby.com</div>
    </div>
  </section>

  <section class="card-back card-back-choc">
    <div class="photo" role="img" aria-label="Photo of a smiling woman biting a chocolate bar, chocolate smeared on her cheek, dark background"></div>
    <div class="choc-copy">
      <div class="lead">Call Now!<br>&amp;</div>
      <div class="sub">Learn how to</div>
      <ul>
        <li>* Drink Bear</li>
        <li>* Eat Chocolate</li>
        <li>* Have Great Sex.</li>
      </ul>
    </div>
  </section>

  <section class="card-back card-back-sea">
    <div class="photo" role="img" aria-label="Side profile photo of a woman about to bite a chocolate-dipped treat against a blue background"></div>
    <div class="sea-copy">Give me a Call<br>And Learn How to<br>Eat Chocolate,<br>Drink Bear and<br>Have Great Sex</div>
    <div class="sea-brand">Harbor</div>
  </section>

</div>
</body>
</html>
```